Business Card Re-Design/Update

We'd like to update out business cards. I've included our current "Style guide" which has the colour scheme of the organisation in it. I've also included the branding files with logos etc in them.

I've also included a copy of one of our existing cards so that you can see how ugly/dated they look. I'd like a fresh modern corporate look.

Target Market(s)

These are for our clients, potential clients, industry contacts - like all business cards

Contact Information for Business Card

Name
Position
Company Address - Level 1, 52 Copperfield Road, Dunmore Qld 4071
Direct Phone
mobile
Email
Website -www.korvelit.com.au
Logo

Colors

Designer to choose colors to be used in the design.

Requirements
Must have
• Main Logo
• Cards will need to be editable to be able to personalize them for each new employee.
Nice to have
• The MapIT, HandIT, KeepIT would be okay to have if they can be sensibly and professionally added to the look without detracting from the main imagery.
• Maybe they could go on the back of the card? will leave this to your creative discretion as to whether/where they fit.
Should not have
• Should not have decorative or script fonts

```html
<!DOCTYPE html>
<html lang="en">
<head>
<meta charset="utf-8">
<title>KorvelIT Business Cards</title>
<link rel="stylesheet" href="https://fonts.googleapis.com/css2?family=Arimo:wght@400;700&family=Nunito:wght@400;700&display=swap">
<style>
  :root {
    --bg: #2b2b2b;
    --card: #ffffff;
    --red: #d0111b;
    --ink: #3a3a3a;
    --grey: #555555;
    --magenta: #c2339c;
    --blue: #2e97d3;
    --green: #6cb33f;
  }
  html, body {
    margin: 0;
    width: 1200px;
    height: 997px;
    overflow: hidden;
    background: var(--bg);
  }
  .canvas {
    position: relative;
    width: 1200px;
    height: 997px;
  }
  .card {
    position: absolute;
    width: 520px;
    height: 316px;
    background: var(--card);
    border-radius: 22px;
    overflow: hidden;
    box-shadow: 0 18px 40px rgba(0,0,0,0.45);
  }

  /* Back card */
  .card--back { left: 60px; top: 190px; }
  .service { position: absolute; left: 0; }
  .service__bar {
    position: absolute; left: 0; top: 0; height: 14px;
  }
  .service__mark {
    position: absolute; top: -4px; width: 18px; height: 18px;
    box-sizing: border-box; border: 3px solid currentColor; border-radius: 2px;
  }
  .service__label {
    position: absolute; top: 24px;
    font-family: "Nunito", sans-serif; font-size: 24px; white-space: nowrap;
  }
  .service__label b { font-weight: 700; }
  .service--keep { top: 70px; color: var(--magenta); }
  .service--keep .service__bar { width: 330px; background: var(--magenta); }
  .service--keep .service__mark { left: 338px; }
  .service--keep .service__label { left: 338px; }
  .service--hand { top: 145px; color: var(--blue); }
  .service--hand .service__bar { width: 250px; background: var(--blue); }
  .service--hand .service__mark { left: 258px; }
  .service--hand .service__label { left: 250px; }
  .service--map { top: 220px; color: var(--green); }
  .service--map .service__bar { width: 170px; background: var(--green); }
  .service--map .service__mark { left: 178px; }
  .service--map .service__label { left: 172px; }

  /* Front card */
  .card--front { left: 620px; top: 440px; }
  .brand {
    position: absolute; left: 34px; top: 118px;
    display: flex; flex-direction: column; align-items: flex-start; gap: 12px;
  }
  .brand__square { width: 40px; height: 40px; background: var(--red); margin-left: 70px; }
  .brand__name {
    font-family: "Nunito", sans-serif; font-weight: 700; font-size: 40px;
    color: var(--ink); line-height: 1;
  }
  .divider {
    position: absolute; left: 262px; top: 50px; width: 2px; height: 200px;
    background: linear-gradient(to bottom, rgba(208,17,27,0), var(--red) 20%, var(--red) 80%, rgba(208,17,27,0));
  }
  .contact {
    position: absolute; left: 282px; top: 52px; right: 14px;
    font-family: "Arimo", sans-serif; color: var(--ink);
  }
  .contact__name { margin: 0; font-size: 16px; font-weight: 700; color: var(--red); letter-spacing: .5px; }
  .contact__role { margin: 2px 0 6px; font-size: 13px; }
  .contact__address { margin: 0 0 12px 14px; font-size: 12px; line-height: 1.35; color: var(--red); font-style: normal; }
  .contact__list { list-style: none; margin: 0 0 0 14px; padding: 0; font-size: 13px; }
  .contact__list li { display: flex; align-items: center; gap: 7px; margin-bottom: 5px; }
  .icon { width: 14px; height: 14px; flex: none; }
  .contact__web { margin: 4px 0 0 14px; font-size: 15px; font-weight: 700; color: var(--red); }
</style>
</head>
<body>
<main class="canvas">

  <section class="card card--back" aria-label="Card back">
    <div class="service service--keep">
      <span class="service__bar"></span><span class="service__mark"></span>
      <span class="service__label">Keep<b>IT</b></span>
    </div>
    <div class="service service--hand">
      <span class="service__bar"></span><span class="service__mark"></span>
      <span class="service__label">Hand<b>IT</b></span>
    </div>
    <div class="service service--map">
      <span class="service__bar"></span><span class="service__mark"></span>
      <span class="service__label">Map<b>IT</b></span>
    </div>
  </section>

  <section class="card card--front" aria-label="Card front">
    <div class="brand">
      <span class="brand__square"></span>
      <span class="brand__name">KorvelIT</span>
    </div>
    <span class="divider"></span>
    <div class="contact">
      <h1 class="contact__name">MARCUS HALLOWAY</h1>
      <p class="contact__role">Director</p>
      <address class="contact__address">Level 1, 52 Copperfield Road,<br>Dunmore Qld 4071</address>
      <ul class="contact__list">
        <li><svg class="icon" viewBox="0 0 14 14"><circle cx="7" cy="7" r="7" fill="#d0111b"/><path d="M4 5.5c1 2 2.5 3.5 4.5 4.5l1-1.2-1.3-.8-.6.6c-.8-.5-1.5-1.2-2-2l.6-.6L5.4 4.7z" fill="#fff"/></svg>1300 555 017</li>
        <li><svg class="icon" viewBox="0 0 14 14"><circle cx="7" cy="7" r="7" fill="#d0111b"/><path d="M4 5.5c1 2 2.5 3.5 4.5 4.5l1-1.2-1.3-.8-.6.6c-.8-.5-1.5-1.2-2-2l.6-.6L5.4 4.7z" fill="#fff"/></svg>+61 7 5550 1842</li>
        <li><svg class="icon" viewBox="0 0 14 14"><circle cx="7" cy="7" r="7" fill="#d0111b"/><rect x="3.5" y="4.5" width="7" height="5" fill="none" stroke="#fff" stroke-width="1"/><path d="M3.5 4.5 7 7.3l3.5-2.8" fill="none" stroke="#fff" stroke-width="1"/></svg>enquiry@korvelit.com.au</li>
      </ul>
      <p class="contact__web">www.korvelit.com.au</p>
    </div>
  </section>

</main>
</body>
</html>
```